Bref créative
Real Estate Sign
BRISK
I need double sided standard sized Business Card [3.5" x 2"]
very SIMPLE, art-deco, upscale look
Simple
Wade Brisk (not on image, Please)
BRISK Real Estate
418 N Walnut Street #5
Sarasota, FL 34871 (not on image, Please)
Wade@HPLmailbox.example
On a business card layout I want to design what I want my real estate sign to look like. Therefore, all I want on the front of the card is: My BRISK logo, the words: Real Estate, 941-382-6150 (my office phone number) & the words: Licensed Real Estate Broker (very small letters)
Same request as above, except vertical design. -- In conclusion, I want one design horizontal and one vertical

```html
<!DOCTYPE html>
<html lang="en">
<head>
<meta charset="utf-8">
<title>BRISK Real Estate – Business Card</title>
<link rel="stylesheet" href="https://fonts.googleapis.com/css2?family=Jost:wght@400&display=swap">
<style>
  :root {
    --navy: #0c2a5c;
    --paper: #ffffff;
    --ink: #1a1a1a;
  }
  * { box-sizing: border-box; margin: 0; padding: 0; }
  html, body {
    width: 1200px;
    height: 686px;
    overflow: hidden;
    background: var(--paper);
  }
  .card {
    position: relative;
    width: 1200px;
    height: 686px;
    background: var(--paper);
    border: 4px solid var(--navy);
    font-family: "Jost", "Futura", sans-serif;
    color: var(--ink);
  }
  .brand {
    position: absolute;
    left: 0;
    top: 34px;
    width: 100%;
    height: 422px;
    display: flex;
    align-items: center;
    justify-content: center;
    gap: 28px;
  }
  .brand-square {
    width: 64px;
    height: 64px;
    background: var(--navy);
  }
  .brand-name {
    font-family: "Jost", "Futura", sans-serif;
    font-weight: 400;
    font-size: 104px;
    letter-spacing: 6px;
    color: var(--navy);
    line-height: 1;
  }
  .tagline {
    position: absolute;
    left: 0;
    width: 100%;
    top: 470px;
    text-align: center;
    font-size: 27px;
    letter-spacing: 0.5px;
  }
  .licence {
    position: absolute;
    left: 0;
    width: 100%;
    top: 516px;
    text-align: center;
    font-size: 12px;
  }
  .address, .contact {
    position: absolute;
    top: 574px;
    font-size: 26px;
    line-height: 43px;
    font-style: normal;
  }
  .address { left: 58px; }
  .contact { right: 44px; }
</style>
</head>
<body>
  <main class="card">
    <div class="brand">
      <span class="brand-square"></span>
      <span class="brand-name">BRISK</span>
    </div>
    <p class="tagline">Real Estate</p>
    <p class="licence">Licensed Real Estate Broker</p>
    <address class="address">
      418 N Walnut Street #5
    </address>
    <div class="contact">
      E-mail: Wade@HPLmailbox.example<br>
      Ph: 941-382-6150
    </div>
  </main>
</body>
</html>
```